Personal Training card design

i am a enthusiastic personal trainer wanting to appeal to as many people as possible.

offering health screening, single or group personal training, geared towards helping the client achieve their goal no matter what it is.

providing a professional service in a top gym facility.

I want to come across professional and trustworthy.

I want my card to be timeless and not look out of date in a years time.

I want the card to be informative and clear about what I offer and display my contact details.

ideally id like the colours blue and white but open to other colour options.

I want the final outcome to communicate professionalism, a PT the clients can trust, and that I can do what I claim.

id like a logo similar to the picture I have provided (the logo on the left hand side) if possible incorporating my initials "OD" or "ODF" but not essential.

Industry/Entity Type

Professional Service

Contact Information for Business Card

OwenDaleyFitness

"Real Results For Every Body"

specializing in
- weight loss & tone
- strength and conditioning
- nutritional advice

Book your free consultation today and take the first step toward achieving your goal!

for details contact me via
email: owendaleyfitness.example.co.uk
phone: 07700954218

or..
visit me via
facebook: owendaleyfitness
twitter: @owendaleyfitness

```html
<!DOCTYPE html>
<html lang="en">
<head>
<meta charset="utf-8">
<title>OwenDaleyFitness business card</title>
<link rel="stylesheet" href="https://fonts.googleapis.com/css2?family=Open+Sans:wght@400;600;700&display=swap">
<style>
:root {
  --page: #eceff3;
  --navy: #0c3a63;
  --blue: #2f7fc4;
  --sky: #6aa9de;
  --white: #ffffff;
  --ink: #111418;
  --muted: #4a525c;
  --bullet: #2f7fc4;
}
* { margin: 0; padding: 0; box-sizing: border-box; }
html, body { width: 1200px; height: 784px; overflow: hidden; }
body {
  background: var(--page);
  font-family: "Open Sans", Arial, sans-serif;
  display: flex;
  align-items: center;
  justify-content: center;
  gap: 40px;
}
.card {
  position: relative;
  width: 540px;
  height: 309px;
  border-radius: 4px;
  overflow: hidden;
  box-shadow: 0 6px 18px rgba(0,0,0,.18);
}

/* back face */
.card-back { color: var(--white); }
.card-back .pattern {
  position: absolute; inset: 0;
  background: radial-gradient(ellipse at 80% 30%, var(--sky) 0%, var(--blue) 45%, var(--navy) 100%);
}
.card-back .brand {
  position: absolute; top: 28px; left: 0; right: 0;
  display: flex; align-items: center; justify-content: center; gap: 10px;
}
.card-back .brand-dot {
  width: 22px; height: 22px; border-radius: 50%;
  background: var(--white);
}
.card-back .brand-name {
  font-weight: 600; font-size: 20px; color: var(--white);
}
.card-back .offer {
  position: absolute; top: 98px; left: 30px; right: 30px;
  text-align: center;
  text-transform: uppercase;
  letter-spacing: 2px;
  font-size: 13px; line-height: 1.5;
}
.card-back .offer strong { font-weight: 700; }
.contact-list {
  position: absolute; top: 170px; right: 40px;
  list-style: none;
  font-size: 15px; line-height: 1.45;
}
.contact-list li { display: flex; align-items: center; gap: 7px; }
.contact-list svg { width: 14px; height: 14px; flex: none; }
.contact-list .social-mark {
  width: 13px; height: 13px; background: var(--white); border-radius: 2px; flex: none;
}

/* front face */
.card-front { background: var(--white); color: var(--ink); }
.card-front .brand {
  position: absolute; top: 40px; left: 30px;
  display: flex; align-items: center; gap: 16px;
}
.card-front .brand-dot {
  width: 70px; height: 70px; border-radius: 50%;
  background: var(--navy); flex: none;
}
.card-front .brand-name {
  font-weight: 600; font-size: 28px; color: var(--navy);
  line-height: 1.1;
}
.card-front .tagline {
  position: absolute; top: 126px; left: 30px;
  font-size: 14px; font-weight: 400; color: var(--muted);
}
.services {
  position: absolute; top: 172px; left: 30px;
  list-style: none;
  font-size: 17px; font-weight: 600; line-height: 1.55;
}
.services li::before {
  content: "•"; color: var(--bullet); margin-right: 9px;
}
</style>
</head>
<body>
  <section class="card card-back">
    <div class="pattern" role="img" aria-label="Blue background with a field of soft light-blue circles"></div>
    <div class="brand">
      <span class="brand-dot"></span>
      <span class="brand-name">OwenDaleyFitness</span>
    </div>
    <p class="offer">Book your <strong>free</strong> consultation today and take the first step toward achieving your goal!</p>
    <ul class="contact-list">
      <li><svg viewBox="0 0 24 24"><path fill="#fff" d="M6.6 10.8a15 15 0 0 0 6.6 6.6l2.2-2.2a1 1 0 0 1 1-.25 11.4 11.4 0 0 0 3.6.57 1 1 0 0 1 1 1V20a1 1 0 0 1-1 1A17 17 0 0 1 3 4a1 1 0 0 1 1-1h3.5a1 1 0 0 1 1 1c0 1.25.2 2.45.57 3.57a1 1 0 0 1-.25 1z"/></svg>07700954218</li>
      <li><svg viewBox="0 0 24 24"><rect x="2" y="5" width="20" height="14" rx="2" fill="#fff"/><path d="M3 6l9 7 9-7" fill="none" stroke="#0c3a63" stroke-width="2"/></svg>owendaleyfitness.example.co.uk</li>
      <li><span class="social-mark"></span>owendaleyfitness</li>
      <li><span class="social-mark"></span>@owendaleyfitness</li>
    </ul>
  </section>

  <section class="card card-front">
    <div class="brand">
      <span class="brand-dot"></span>
      <span class="brand-name">OwenDaleyFitness</span>
    </div>
    <p class="tagline">Real results for every body</p>
    <ul class="services">
      <li>Weight loss &amp; Tone</li>
      <li>Strength &amp; Conditioning</li>
      <li>Nutrition &amp; Diet advice</li>
      <li>For One to One or Group Personal Training</li>
    </ul>
  </section>
</body>
</html>
```